We need an attractive business card design that is modern and inviting. We like the blue and yellow (or gold) colors that are displayed with the logo. The business should communicate trust, experience, and integrity.

Target Market(s)

Residential and Commercial

Industry/Entity Type

Business

Contact Information for Business Card

Recessed Lighting
LED Retro Fit
Sign Repair
Alarms and Cameras
Mobile Home Services
24hr service calls

Font styles to use
Serif
Sans Serif

Colors
3176b5
0455a3
fece3e
fbee3e

Requirements
Must have
• Brondle Electric
• Owner: Marcus Tivane
• Licensed and Insured
• TECL #58917
Nice to have
• Exquisite Detail!!
• Over 20 years of experience
Should not have
• Nothing boring or traditional!!!

```html
<!DOCTYPE html>
<html lang="en">
<head>
<meta charset="utf-8">
<title>Brondle Electric — Business Card</title>
<link rel="stylesheet" href="https://fonts.googleapis.com/css2?family=Arimo:wght@400;700&family=Libre+Baskerville:wght@700&display=swap">
<style>
  :root {
    --bg: #2a2a2c;
    --card: #060606;
    --yellow: #e2e232;
    --gold: #fece3e;
    --blue: #1c5ea8;
    --blue-light: #3176b5;
    --white: #f2f2f2;
  }
  * { box-sizing: border-box; margin: 0; padding: 0; }
  html, body {
    width: 1200px; height: 997px; overflow: hidden;
    background: var(--bg);
    font-family: "Arimo", Arial, sans-serif;
  }
  .sheet {
    position: relative; width: 1200px; height: 997px;
  }
  .card {
    position: absolute; left: 240px;
    width: 720px; height: 411px;
    background: var(--card);
    border-radius: 26px;
    overflow: hidden;
  }
  .card--back { top: 70px; }
  .card--front { top: 516px; }
  .card__bands {
    position: absolute; inset: 0; width: 100%; height: 100%;
  }
  .band--yellow { fill: var(--yellow); }
  .band--blue { fill: var(--blue); }

  /* logo lockup */
  .brand {
    position: absolute; display: flex; align-items: center; gap: 14px;
  }
  .brand__mark {
    width: 58px; height: 58px; border-radius: 50%;
    border: 5px solid var(--blue);
  }
  .brand__name {
    font-weight: 700; font-size: 30px; letter-spacing: 1px;
    color: var(--yellow); white-space: nowrap;
  }
  .card--back .brand {
    left: 52px; top: 140px;
    flex-direction: column; align-items: center; gap: 10px;
  }
  .card--back .brand__name { font-size: 26px; }
  .card--front .brand { right: 48px; top: 44px; }

  /* services list */
  .services {
    position: absolute; left: 410px; top: 70px;
    list-style: none;
  }
  .services li {
    position: relative; padding-left: 20px;
    font-size: 19px; line-height: 32px; color: var(--yellow);
    white-space: nowrap;
  }
  .services li::before {
    content: ""; position: absolute; left: 0; top: 13px;
    width: 7px; height: 7px; border-radius: 50%; background: var(--yellow);
  }
  .services li:nth-child(even) { color: var(--blue-light); }
  .services li:nth-child(odd)::before { background: var(--blue-light); }
  .services li:nth-child(even)::before { background: var(--yellow); }

  /* owner */
  .owner { position: absolute; left: 40px; top: 150px; }
  .owner__name {
    font-family: "Libre Baskerville", Georgia, serif;
    font-weight: 700; font-size: 34px; color: var(--yellow);
  }
  .owner__title {
    margin-top: 4px; font-weight: 700; font-size: 16px;
    letter-spacing: 1px; color: var(--white);
  }

  .credentials {
    position: absolute; right: 52px; top: 200px;
    text-align: right; font-size: 18px; line-height: 30px; color: var(--yellow);
  }

  /* contact */
  .contact__tab {
    position: absolute; left: 0; top: 262px;
    width: 52px; height: 108px;
    background: var(--blue); border-radius: 0 14px 14px 0;
    display: flex; flex-direction: column; align-items: center;
    justify-content: space-around; padding: 8px 0;
  }
  .contact__tab svg { width: 20px; height: 20px; fill: none; stroke: var(--white); stroke-width: 2; }
  .contact__list {
    position: absolute; left: 66px; top: 264px; list-style: none;
  }
  .contact__list li {
    font-size: 20px; line-height: 34px; color: var(--white);
  }
</style>
</head>
<body>
<main class="sheet">

  <section class="card card--back" aria-label="Card back with services">
    <svg class="card__bands" viewBox="0 0 720 411" preserveAspectRatio="none" aria-hidden="true">
      <polygon class="band--yellow" points="0,398 478,364 470,411 0,411"/>
      <path class="band--blue" d="M484,364 Q490,342 510,340 L720,322 L720,411 L474,411 Z"/>
    </svg>
    <div class="brand">
      <span class="brand__mark" aria-hidden="true"></span>
      <span class="brand__name">BRONDLE ELECTRIC</span>
    </div>
    <ul class="services">
      <li>Residential and Commercial</li>
      <li>Recessed Lighting</li>
      <li>LED Retro Fit</li>
      <li>Sign Repair</li>
      <li>Alarms and Cameras</li>
      <li>Mobile Home Services</li>
      <li>24hr service calls</li>
    </ul>
  </section>

  <section class="card card--front" aria-label="Card front with contact details">
    <svg class="card__bands" viewBox="0 0 720 411" preserveAspectRatio="none" aria-hidden="true">
      <polygon class="band--yellow" points="0,398 478,364 470,411 0,411"/>
      <path class="band--blue" d="M484,364 Q490,342 510,340 L720,322 L720,411 L474,411 Z"/>
    </svg>
    <div class="brand">
      <span class="brand__mark" aria-hidden="true"></span>
      <span class="brand__name">BRONDLE ELECTRIC</span>
    </div>
    <div class="owner">
      <p class="owner__name">Marcus Tivane</p>
      <p class="owner__title">OWNER</p>
    </div>
    <div class="credentials">
      <p>Licensed and Insured</p>
      <p>TECL #58917</p>
    </div>
    <div class="contact__tab" aria-hidden="true">
      <svg viewBox="0 0 20 20"><rect x="5" y="1.5" width="10" height="17" rx="2"/><line x1="9" y1="15.5" x2="11" y2="15.5"/></svg>
      <svg viewBox="0 0 20 20"><rect x="2" y="4.5" width="16" height="11"/><polyline points="2,4.5 10,11 18,4.5"/></svg>
      <svg viewBox="0 0 20 20"><path d="M8.5 11.5 L11.5 8.5"/><path d="M7 9.5 L4.5 12 a2.5 2.5 0 0 0 3.5 3.5 L10.5 13"/><path d="M13 10.5 L15.5 8 a2.5 2.5 0 0 0 -3.5 -3.5 L9.5 7"/></svg>
    </div>
    <ul class="contact__list">
      <li>289-555-0147</li>
      <li>mt@brondleelectric.com</li>
      <li>www.brondleelectric.com</li>
    </ul>
  </section>

</main>
</body>
</html>
```